K7 seamless

We are a glazing company specializing in frameless glass .
I would like the business cards in black with the logo taking up the most part of the front added with " frameless glass specialist's " below it.
On the back side I would like a list of what we do :
• shower screens
• glass balustrade / pool fencing
• mirrors
•office partitions
• sky lights
•shop fronts
•splash backs
Also include this information :
📧 - corbin@k7seamless.com
📞Corbin - 0418276594
📞 Milo - 0427 613 508
Updates
To all designs already posted can you include on the back of the card in the services part -
•splash backs
Target Market(s)
High end builders
Industry/Entity Type
Glazing
Contact Information for Business Card
On the back side I would like a list of what we do : • shower screens • glass balustrade / pool fencing • mirrors •office partitions • sky lights •shop fronts Also include this information : 📧 - corbin@k7seamless.com 📞Corbin - 0418276594 📞 Milo - 0427 613 508
Colors
Designer to choose colors to be used in the design.
Look and feel
Each slider illustrates characteristics of the customer's brand and the style your logo design should communicate.

```html
<!DOCTYPE html>
<html lang="en">
<head>
<meta charset="utf-8">
<title>K7 seamless – Business Cards</title>
<link rel="stylesheet" href="https://fonts.googleapis.com/css2?family=Open+Sans:wght@400;600;700;800&display=swap">
<style>
  :root {
    --stage: #232324;
    --card: #1e1e22;
    --teal: #1fb5ac;
    --mint: #6fcb9c;
    --white: #ffffff;
    --ghost: #29292e;
    --font: "Open Sans", Arial, sans-serif;
  }
  * { margin: 0; padding: 0; box-sizing: border-box; }
  html, body {
    width: 1200px; height: 780px; overflow: hidden;
    background: var(--stage);
    font-family: var(--font);
  }
  .stage {
    width: 1200px; height: 780px;
    display: flex; align-items: center; justify-content: center; gap: 40px;
  }
  .card {
    position: relative;
    width: 540px; height: 310px;
    background: var(--card);
    overflow: hidden;
    box-shadow: 0 18px 40px rgba(0,0,0,.55);
  }

  /* Contact side */
  .contact-card .brand {
    position: absolute; left: 0; right: 0; top: 34px;
    display: flex; align-items: center; justify-content: center; gap: 12px;
  }
  .contact-card .brand-mark {
    width: 20px; height: 20px; background: var(--teal); flex: none;
  }
  .contact-card .brand-name {
    font-size: 42px; font-weight: 800; color: var(--teal);
    letter-spacing: -0.5px; line-height: 1;
  }
  .ghost-name {
    position: absolute; left: 96px; top: 226px;
    font-size: 62px; font-weight: 800; color: var(--ghost);
    line-height: 1; letter-spacing: -1px; white-space: nowrap;
  }
  .contact-list {
    position: absolute; left: 34px; top: 124px;
    list-style: none;
  }
  .contact-list li {
    display: flex; align-items: center; gap: 8px;
    font-size: 15px; font-weight: 600; color: var(--white);
    margin-bottom: 9px; line-height: 1.2;
  }
  .contact-list .who { color: var(--mint); font-weight: 400; }
  .contact-list svg { width: 14px; height: 14px; fill: var(--teal); flex: none; }
  .people {
    position: absolute; right: 50px; top: 118px;
    text-align: right;
    font-size: 38px; font-weight: 700; line-height: 1.05;
    color: var(--mint);
  }
  .edge-band {
    position: absolute; right: 0; top: 118px;
    width: 26px; height: 84px;
    background: linear-gradient(180deg, var(--mint), var(--teal));
  }

  /* Services side */
  .services-card .brand-name {
    position: absolute; left: 0; right: 0; top: 70px;
    text-align: center;
    font-size: 58px; font-weight: 800; color: var(--teal);
    letter-spacing: -1px; line-height: 1;
  }
  .services-heading {
    position: absolute; left: 0; right: 0; top: 176px;
    text-align: center;
    font-size: 15px; font-weight: 600; color: var(--teal);
    letter-spacing: .5px;
  }
  .services-list {
    position: absolute; left: 20px; right: 20px; top: 206px;
    list-style: none; text-align: center;
    font-size: 12px; color: var(--white); line-height: 1.9;
    text-transform: uppercase;
  }
  .services-list li { display: inline; }
  .services-list li + li::before {
    content: ""; display: inline-block;
    width: 7px; height: 7px; border-radius: 50%;
    background: var(--teal); margin: 0 6px 1px;
  }
  .services-list .row-start::before { display: none; }
  .services-list .row-break { display: block; height: 0; }
  .services-list .row-break::before { display: none; }
</style>
</head>
<body>
<main class="stage">

  <section class="card contact-card" aria-label="Business card contact side">
    <span class="ghost-name" aria-hidden="true">K7 seamless</span>
    <div class="brand">
      <span class="brand-mark" aria-hidden="true"></span>
      <h1 class="brand-name">K7 seamless</h1>
    </div>

    <ul class="contact-list">
      <li>
        <svg viewBox="0 0 24 24" aria-hidden="true"><path d="M6.6 10.8a15.1 15.1 0 0 0 6.6 6.6l2.2-2.2a1 1 0 0 1 1-.25 11.4 11.4 0 0 0 3.6.57 1 1 0 0 1 1 1V20a1 1 0 0 1-1 1A17 17 0 0 1 3 4a1 1 0 0 1 1-1h3.5a1 1 0 0 1 1 1c0 1.25.2 2.45.57 3.57a1 1 0 0 1-.25 1z"/></svg>
        0418276594 <span class="who">(Corbin)</span>
      </li>
      <li>
        <svg viewBox="0 0 24 24" aria-hidden="true"><path d="M6.6 10.8a15.1 15.1 0 0 0 6.6 6.6l2.2-2.2a1 1 0 0 1 1-.25 11.4 11.4 0 0 0 3.6.57 1 1 0 0 1 1 1V20a1 1 0 0 1-1 1A17 17 0 0 1 3 4a1 1 0 0 1 1-1h3.5a1 1 0 0 1 1 1c0 1.25.2 2.45.57 3.57a1 1 0 0 1-.25 1z"/></svg>
        0427 613 508 <span class="who">(Milo)</span>
      </li>
      <li>
        <svg viewBox="0 0 24 24" aria-hidden="true"><path d="M3 5h18a1 1 0 0 1 1 1v12a1 1 0 0 1-1 1H3a1 1 0 0 1-1-1V6a1 1 0 0 1 1-1zm1 2.4V17h16V7.4l-8 5.2z"/></svg>
        corbin@k7seamless.com
      </li>
    </ul>

    <p class="people">Corbin<br>Milo</p>
    <span class="edge-band" aria-hidden="true"></span>
  </section>

  <section class="card services-card" aria-label="Business card services side">
    <h2 class="brand-name">K7 seamless</h2>
    <p class="services-heading">WHAT WE DO</p>
    <ul class="services-list">
      <li>Shower screens</li>
      <li>Glass balustrade / pool fencing</li>
      <li>Mirrors</li>
      <li class="row-break" aria-hidden="true"></li>
      <li class="row-start">Office partitions</li>
      <li>Sky lights</li>
      <li>Shop fronts</li>
      <li>Splash backs</li>
    </ul>
  </section>

</main>
</body>
</html>
```